Campaign Flyer for a local election

Black and white election flyer

See information below to be included:

Re-elect Morton
Experienced Glenmoor Board Member
Experienced NYC Principal
Experienced leader

One Year Board Accomplishments:
-Installed New Park Lights (Bollards)
-Red Brick Road Repair Project
-Established Closer Ties with Our local precinct to frequently monitor the community with directed security patrols. Requested an increased police presence.
-Met with the 82nd Precinct Officials & Assemblywoman, Linda Marwick to discuss our security issues
- Focused on maintenance of streetlights to make brighter streets
-Negotiated Contract & Hired Our New Landscaper, Hollowfield Landscapers
-Major Homeowner Shrub Replacement Project
- Addressing Standing Water in our Park (Installed French Drain)
- Replaced and upgraded all 5 outdoor circuit breaker panels
-Write monthly community newsletters
-Sewer cleaning project (had all community catch basins cleaned)
-Carefully overseeing our new school project. Coordinating with the sponsor and the school directors
-Delivered a very healthy budget to the community
-Works closely with our committees
-Events: Zoo event, Petting Zoo, Outdoor Movie Night, Egg Hunt

It is my intent to seek re-election.
(Photo) Morton Velasquez
-Dedicated to improving our community
-Hard-working…He gets thing done!
-Trustworthy

. .

Please note, I am submitting new information under accomplishments. The list of accomplishments should be in the same sequence, starting with: Met with the 82nd Precinct....
Please carefully review.
----------------------------------------------------------------------------------------------------------------------------------------------------------------

Re-elect Morton
Experienced NYC Principal
Experienced leader

Last Year’s Board Accomplishments:

-Met with the 82nd Precinct Officials & Assemblywoman, Linda Marwick, to discuss our security issues. Requested increased police presence.
-Established a strong partnership with the 82nd precinct to frequently monitor the community with directed security patrols.
-Replaced all new park lights (Bollards) to make the park brighter
- Focused on maintenance of streetlights to make streets brighter
-‘Fixing Our Streets Project’ (Repaired all cracked/missing red bricks)
-Homeowner Shrub Replacement Project (Replaced hundreds of bushes)
- I write the monthly community newsletter
-Carefully overseeing our new school project. Coordinating with the sponsor and the school director
-Monitoring C of O’s and homeowners Insurance

(Photo) Morton Velasquez
-Hard-working! I get things done!
-Trustworthy

. .

Re-elect Morton
Experienced NYC Principal
Experienced leader

(Photo) Morton Velasquez
-Trustworthy

. .

Target Market(s)

A Community electing a Board Member

Industry/Entity Type

residential election

Requirements
Must have
• all black, white and grey print. Flyers will not be printed in color
Nice to have
• See the information in the attachment below containing all my accomplishments
Should not have
• color

```html
<!DOCTYPE html>
<html lang="en">
<head>
<meta charset="utf-8">
<title>Re-elect Morton – Campaign Flyer</title>
<link rel="stylesheet" href="https://fonts.googleapis.com/css2?family=Oswald:wght@500;600&family=Open+Sans:wght@400;600;700;800&display=swap">
<style>
  :root{
    --page-bg:#e9e9e9;
    --paper:#ffffff;
    --ink:#1e1e1e;
    --ink-soft:#2f2f2f;
    --title-grey:#5a5a5a;
    --band-grey:#767676;
    --ring-grey:#7d7d7d;
    --wash-grey:#d9d9d9;
    --bullet-grey:#8a8a8a;
    --photo-light:#c4c4c4;
    --photo-dark:#4a4a4a;
  }
  *{box-sizing:border-box;margin:0;padding:0}
  html,body{width:1200px;height:1200px;overflow:hidden;background:var(--page-bg)}
  .flyer{
    position:absolute;left:179px;top:8px;width:843px;height:1184px;
    background:var(--paper);overflow:hidden;
    font-family:"Open Sans",Arial,sans-serif;color:var(--ink-soft);
  }
  .credentials-band{
    position:absolute;left:0;top:127px;width:480px;height:121px;z-index:1;
    background:var(--band-grey);
  }
  .portrait-art{position:absolute;left:0;top:0;width:843px;height:640px;z-index:2}
  .headline{
    position:absolute;left:47px;top:40px;z-index:3;white-space:nowrap;
    font-family:"Oswald",Impact,sans-serif;font-weight:600;
    font-size:68px;line-height:1;color:var(--title-grey);
    transform:scaleX(.83);transform-origin:left top;
  }
  .credentials{
    position:absolute;left:48px;top:142px;z-index:3;
    color:#fff;font-weight:700;font-size:21px;line-height:30px;white-space:nowrap;
  }
  .accomplishments{position:absolute;left:48px;top:274px;z-index:3;width:770px}
  .accomplishments h2{font-size:20px;font-weight:700;color:var(--ink);margin-bottom:8px;line-height:26px}
  .accomplishments ul{list-style:none}
  .accomplishments li{
    position:relative;padding-left:28px;font-size:17.5px;line-height:24px;
    margin-bottom:10px;color:var(--ink-soft);
  }
  .accomplishments li.justify{text-align:justify}
  .accomplishments li::before{
    content:"";position:absolute;left:2px;top:6px;width:13px;height:13px;
    border-radius:50%;background:var(--bullet-grey);
  }
  .accomplishments li::after{
    content:"";position:absolute;left:6px;top:8px;width:3px;height:6px;
    border:solid #fff;border-width:0 2px 2px 0;transform:rotate(45deg);
  }
  .intent-band{
    position:absolute;left:0;top:968px;width:843px;height:56px;
    background:var(--band-grey);color:#fff;text-align:center;
    font-weight:800;font-size:37px;line-height:56px;letter-spacing:-.3px;
  }
  .candidate-name{
    position:absolute;left:47px;top:1034px;white-space:nowrap;
    font-family:"Oswald",Impact,sans-serif;font-weight:500;
    font-size:64px;line-height:71px;color:var(--ink);
    transform:scaleX(.85);transform-origin:left top;
  }
  .qualities{position:absolute;left:319px;top:1046px;list-style:none}
  .qualities li{
    position:relative;padding-left:33px;font-weight:700;font-size:22px;
    line-height:39px;color:var(--ink-soft);white-space:nowrap;
  }
  .qualities svg{position:absolute;left:0;top:10px}
  .qualities .connector{
    position:absolute;left:9px;top:30px;height:66px;
    border-left:2px dotted var(--ink-soft);
  }
</style>
</head>
<body>
<main class="flyer">
  <div class="credentials-band"></div>

  <svg class="portrait-art" viewBox="0 0 843 640">
    <defs>
      <radialGradient id="photoTone" cx="45%" cy="40%" r="70%">
        <stop offset="0" stop-color="var(--photo-light)"/>
        <stop offset="1" stop-color="var(--photo-dark)"/>
      </radialGradient>
    </defs>
    <path d="M570 0 H843 V360 Q760 220 640 80 Z" fill="var(--wash-grey)"/>
    <circle cx="724" cy="313" r="286" fill="var(--ring-grey)"/>
    <circle cx="730" cy="305" r="278" fill="var(--paper)"/>
    <g role="img" aria-label="Black and white portrait photo of candidate Morton Velasquez">
      <circle cx="734" cy="302" r="270" fill="url(#photoTone)"/>
    </g>
  </svg>

  <h1 class="headline">RE-ELECT MORTON</h1>

  <div class="credentials">
    <p>Experienced Glenmoor Board Member</p>
    <p>Experienced NYC Principal</p>
    <p>Experienced leader</p>
  </div>

  <section class="accomplishments">
    <h2>One Year Board Accomplishments:</h2>
    <ul>
      <li>Installed New Park Lights (Bollards)</li>
      <li>Red Brick Road Repair Project</li>
      <li style="max-width:370px">Focused on maintenance of streetlights to make brighter streets</li>
      <li style="max-width:380px">Negotiated Contract and Hired Our New Landscaper, Hollowfield Landscapers</li>
      <li>Major Homeowner Shrub Replacement Project</li>
      <li class="justify" style="max-width:438px">Replaced and upgraded all 5 outdoor circuit breaker panels</li>
      <li>Write monthly community newsletters</li>
      <li>Addressing Standing Water in our Park (Installed French Drain)</li>
      <li>Sewer cleaning project (had all community catch basins cleaned)</li>
      <li>Established Closer Ties with Our local precinct to frequently monitor the community with directed security patrols. Requested an increased police presence.</li>
      <li>Met with the 82nd Precinct Officials and Assemblywoman, Linda Marwick to discuss our security issues</li>
      <li>Carefully overseeing our new school project. Coordinating with the sponsor and the school directors</li>
      <li>Delivered a very healthy budget to the community</li>
      <li>Works closely with our committees</li>
      <li>Events: Zoo event, Petting Zoo, Outdoor Movie Night, Egg Hunt</li>
    </ul>
  </section>

  <div class="intent-band">IT IS MY INTENT TO SEEK RE-ELECTION</div>

  <p class="candidate-name">MORTON<br>VELASQUEZ</p>

  <ul class="qualities">
    <span class="connector"></span>
    <li><svg width="20" height="20" viewBox="0 0 20 20"><circle cx="10" cy="10" r="8" fill="#fff" stroke="#555" stroke-width="1.6"/><path d="M6 10 l3 3 l7 -8" fill="none" stroke="#555" stroke-width="1.8"/></svg>Dedicated to improving our community</li>
    <li><svg width="20" height="20" viewBox="0 0 20 20"><circle cx="10" cy="10" r="8" fill="#fff" stroke="#555" stroke-width="1.6"/><path d="M6 10 l3 3 l7 -8" fill="none" stroke="#555" stroke-width="1.8"/></svg>Hard-working...He gets thing done!</li>
    <li><svg width="20" height="20" viewBox="0 0 20 20"><circle cx="10" cy="10" r="8" fill="#fff" stroke="#555" stroke-width="1.6"/><path d="M6 10 l3 3 l7 -8" fill="none" stroke="#555" stroke-width="1.8"/></svg>Trustworthy</li>
  </ul>
</main>
</body>
</html>
```